14 years in business and its time for a new look and feel brochure and business cards!

We are looking to create a brochure that is professional and eye catching to bring in new commercial business. After14 years in business we have finally redone our logo and it is time to get a brochure completed as well. The logo that should be used is the one that says Inc. We want this new brochure to appeal to corporate property management companies and smaller apartment complexes. We want it to look rich and have the same high quality our work has.

Target Market(s)

property management companies and apartment complexes in the DMV.

Industry/Entity Type

Construction Company

Contact Information for Business Card

Logo
Dovid Markel
CEO
Mobile 410-555-0187
Office 410-555-0142
Address 3417 Harlow Lane Suite C Baltimore, MD 21290
Email DM@BrightCoatProsInc.example

Font styles to use
Sans Serif

Requirements
Must have
• Want the background to be black and silver gradient. Will be printing on high gloss and would like for it to be rich looking.
• brochure will be 8.5x11. open minded in terms of the fold, how it looks best with the design provided will determine that. Can be bi-fold, try-fold or z-fold.
• Content for brochure:About us
• Founded in 2003, BrightCoat Pros Inc. was the vision of Dovid Markel, with a commitment to becoming the premier renovator and developer of residential and commercial properties in the DMV. Today, BrightCoat Pros Inc. is widely respected for their gold standard in quality and efficiency and continues to grow by attracting the highest level of professionals with knowledge and experience in our field.
• BrightCoat Pros Inc.’s most valuable asset is our team members. The efforts they put forth are the key to meeting our standards and providing all of our valued clients with the highest quality of service. Leading our wonderful team members is a group of management like no other. With years of experience, the power to motivate and the keen eye to ensure top quality, our team of experts focus all of their energy to exceed our client’s expectations.
• Our Mission
• We strive to provide timely delivery, the highest level of quality and value on every project. We offer unsurpassed dedication to maintain our working relationships and consistently deliver the best service to ensure our clients success.
• Property Renovations
• BrightCoat Pros Inc. has been responsible for coordinating the construction and renovation of many projects, including all parts of a building’s interior and exterior. Well known for attention to details, quality and timely execution, BrightCoat Pros Inc. has managed and executed more than 4,000 turnovers and over 150 projects in the last 3 years alone.
• Renovations not only improve the appeal and marketability of your property, but also add value. Interior and exterior renovations help make any property more functional, energy-efficient and enable you to keep up with what your market demands. From the smallest change of a door knob to a complete kitchen overhaul, these are the things that make all the difference in your property. We are committed to deliver great value, and we do that by ensuring that our experts are involved in the renovation process, providing input and quality maintenance throughout the entire renovation.
• Services Include
• Painting
• Flooring
• Sub-Flooring
• Crown molding
• Siding & Wood Replacement
• Trim & Carpentry Work
• Punches
• Decks
• Power wash
• Concrete & Paving
• Turnovers including plumbing and electric
• Kitchen overhauls
• We offer first time clients a free apartment paint or punch on us to show you the quality you can always expect!
• Call today to schedule your first-time paint or punch at 410-555-0142.

```html
<!DOCTYPE html>
<html lang="en">
<head>
<meta charset="utf-8">
<title>BrightCoat Pros Inc. – Business Card</title>
<link rel="stylesheet" href="https://fonts.googleapis.com/css2?family=Montserrat:wght@500;600;700&display=swap">
<style>
  :root{
    --page:#ffffff;
    --black:#000000;
    --panel:#111111;
    --blue:#2d5b96;
    --blue-dark:#244b7d;
    --white:#ffffff;
    --photo-a:#2a2a28;
    --photo-b:#1a1a19;
  }
  *{margin:0;padding:0;box-sizing:border-box}
  html,body{width:1200px;height:1200px;overflow:hidden;background:var(--page)}
  body{position:relative;font-family:"Montserrat",sans-serif;color:var(--white)}

  .card{position:absolute;left:181px;width:839px;height:479px;overflow:hidden}
  .card--front{top:91px;background:var(--black)}
  .card--back{top:626px;background:var(--black)}

  .front-photo{position:absolute;left:0;top:0;width:100%;height:355px;
    background:linear-gradient(160deg,#3a3a37 0%,var(--photo-a) 45%,var(--photo-b) 100%)}
  .front-band{position:absolute;left:0;top:355px;width:100%;height:24px;background:var(--blue)}
  .front-web{position:absolute;left:0;top:379px;width:100%;height:100px;display:flex;align-items:center;justify-content:center;
    font-size:22px;font-weight:500;letter-spacing:.5px}

  .brand{position:absolute;left:0;width:100%;display:flex;align-items:center;justify-content:center;gap:12px;
    font-weight:700;color:var(--white);letter-spacing:1px;white-space:nowrap}
  .brand__dot{border-radius:50%;background:var(--white);flex:none}
  .card--front .brand{top:150px;font-size:30px}
  .card--front .brand__dot{width:22px;height:22px}
  .card--back .brand{top:92px;font-size:26px}
  .card--back .brand__dot{width:18px;height:18px}

  .back-top{position:absolute;left:0;top:0;width:100%;height:217px;background:var(--panel)}
  .back-person{position:absolute;left:0;top:235px;width:411px;height:225px;background:var(--panel)}
  .person__bar{position:absolute;left:85px;top:83px;width:10px;height:59px;background:var(--blue)}
  .person__name{position:absolute;left:110px;top:77px;font-size:32px;font-weight:600;line-height:1;white-space:nowrap}
  .person__role{position:absolute;left:110px;top:117px;font-size:26px;font-weight:500;line-height:1;letter-spacing:.5px}

  .contact{position:absolute;left:428px;width:411px;height:61px;
    background:linear-gradient(180deg,var(--blue) 0%,var(--blue) 80%,var(--blue-dark) 100%);
    display:flex;align-items:center}
  .contact--address{top:235px}
  .contact--phone{top:317px}
  .contact--web{top:399px}
  .contact__icon{position:absolute;left:13px;top:10px;width:40px;height:40px;border-radius:50%;background:var(--black);
    display:flex;align-items:center;justify-content:center}
  .contact__text{position:absolute;left:90px;font-size:19px;font-weight:500;line-height:1.25;letter-spacing:.4px;white-space:nowrap}
  .contact--web .contact__text{font-size:17px;letter-spacing:.1px}
</style>
</head>
<body>

<section class="card card--front">
  <div class="front-photo" role="img" aria-label="Dimly lit modern office lobby with reception desk and seating"></div>
  <div class="brand"><span class="brand__dot"></span>BRIGHTCOAT PROS INC.</div>
  <div class="front-band"></div>
  <div class="front-web">www.brightcoatprosinc.example</div>
</section>

<section class="card card--back">
  <div class="back-top"></div>
  <div class="brand"><span class="brand__dot"></span>BRIGHTCOAT PROS INC.</div>

  <div class="back-person">
    <span class="person__bar"></span>
    <p class="person__name">DOVID MARKEL</p>
    <p class="person__role">DIRECTOR</p>
  </div>

  <div class="contact contact--address">
    <span class="contact__icon">
      <svg width="20" height="24" viewBox="0 0 20 24"><path d="M10 1a8 8 0 0 0-8 8c0 6 8 14 8 14s8-8 8-14a8 8 0 0 0-8-8z" fill="#fff"/><circle cx="10" cy="9" r="3" fill="#000"/></svg>
    </span>
    <p class="contact__text">3417 Harlow Lane<br>Baltimore, Maryland</p>
  </div>

  <div class="contact contact--phone">
    <span class="contact__icon">
      <svg width="22" height="22" viewBox="0 0 24 24"><path d="M6.6 10.8a15 15 0 0 0 6.6 6.6l2.2-2.2a1 1 0 0 1 1-.25 11.4 11.4 0 0 0 3.6.57 1 1 0 0 1 1 1V20a1 1 0 0 1-1 1A17 17 0 0 1 3 4a1 1 0 0 1 1-1h3.5a1 1 0 0 1 1 1c0 1.25.2 2.45.57 3.570a1 1 0 0 1-.25 1z" fill="#fff"/></svg>
    </span>
    <p class="contact__text">+1 410-555-0187</p>
  </div>

  <div class="contact contact--web">
    <span class="contact__icon">
      <svg width="22" height="22" viewBox="0 0 24 24" fill="none" stroke="#fff" stroke-width="1.6"><circle cx="12" cy="12" r="10"/><ellipse cx="12" cy="12" rx="4.5" ry="10"/><path d="M2 12h20M4 6.5h16M4 17.5h16"/></svg>
    </span>
    <p class="contact__text">www.brightcoatprosinc.example</p>
  </div>
</section>

</body>
</html>
```